Business Card for Vorlo Parts Wholesale supplier

Hi There! I need a new business card for our company. We are specialized in selling Vorlo parts, mostly we sell new LCD screens for uDialr and oTabs. I would like to see that back in the design.

You can find the colors and logo's on our website: www.darvok.nl

Industry/Entity Type

Business

Contact Information for Business Card

My Details:
Bas Hollink

Phone: 0031627381946
E-mail: Bas@darvok.nl

Slogan: "Because Quality Matters"

Font styles to use
Sans Serif

Colors

Designer to choose colors to be used in the design.

Requirements
Must have
• A Black backside with the Darvok logo on it. The front side should be clean with only my contact details.
• But I'm also open for something really different or awesome!
Nice to have
• Remember that we are in the parts & repairing industry, So i'll be handing those business cards mainly to repair companies. Maybe you can do something with that thought :)

```html
<!DOCTYPE html>
<html lang="en">
<head>
<meta charset="utf-8">
<title>Darvok – Business Card</title>
<link rel="stylesheet" href="https://fonts.googleapis.com/css2?family=Play:wght@400;700&display=swap">
<style>
  :root {
    --page-bg: #d9d6d1;
    --card-bg: #f1f0ee;
    --card-edge: #ffffff;
    --accent: #d24a1e;
    --accent-deep: #c23a12;
    --ink: #1a1a1a;
    --tab: #222222;
  }
  * { margin: 0; padding: 0; box-sizing: border-box; }
  html, body {
    width: 1200px;
    height: 969px;
    overflow: hidden;
    background: var(--page-bg);
  }
  .canvas {
    position: relative;
    width: 1200px;
    height: 969px;
  }
  .card {
    position: absolute;
    left: 187px;
    top: 247px;
    width: 873px;
    height: 495px;
    background: var(--card-bg);
    border: 1px solid var(--card-edge);
    font-family: "Play", sans-serif;
    color: var(--ink);
  }
  .logo-area {
    position: absolute;
    left: 45px;
    top: 41px;
    width: 420px;
    height: 417px;
    background: linear-gradient(135deg, var(--accent), var(--accent-deep));
  }
  .card-tab {
    position: absolute;
    right: 0;
    top: 83px;
    width: 14px;
    height: 45px;
    background: var(--tab);
    border-radius: 4px 0 0 4px;
  }
  .holder-name {
    position: absolute;
    right: 55px;
    top: 84px;
    font-size: 36px;
    line-height: 1;
    font-weight: 700;
    color: var(--accent-deep);
    letter-spacing: 0.5px;
  }
  .contact-list {
    position: absolute;
    right: 58px;
    top: 226px;
    list-style: none;
    text-align: right;
  }
  .contact-item {
    display: flex;
    justify-content: flex-end;
    align-items: center;
    gap: 10px;
    height: 34px;
    font-size: 22px;
  }
  .contact-icon {
    width: 20px;
    height: 20px;
    fill: var(--accent);
    flex: none;
  }
  .brand-name {
    position: absolute;
    right: 55px;
    top: 338px;
    font-size: 100px;
    font-weight: 700;
    line-height: 1;
    color: var(--ink);
    letter-spacing: 1px;
  }
</style>
</head>
<body>
<div class="canvas">
  <section class="card" aria-label="Darvok business card, front">
    <div class="logo-area" role="img" aria-label="Darvok brand mark area"></div>
    <span class="card-tab"></span>
    <h1 class="holder-name">Bas Hollink</h1>
    <ul class="contact-list">
      <li class="contact-item">
        <span>0031627381946</span>
        <svg class="contact-icon" viewBox="0 0 24 24" aria-hidden="true"><path d="M6.6 10.8c1.4 2.8 3.8 5.2 6.6 6.6l2.2-2.2c.3-.3.7-.4 1-.2 1.1.4 2.3.6 3.6.6.6 0 1 .4 1 1V20c0 .6-.4 1-1 1C10.6 21 3 13.4 3 4c0-.6.4-1 1-1h3.5c.6 0 1 .4 1 1 0 1.3.2 2.5.6 3.6.1.3 0 .7-.2 1z"/></svg>
      </li>
      <li class="contact-item">
        <span>Bas@darvok.nl</span>
        <svg class="contact-icon" viewBox="0 0 24 24" aria-hidden="true"><path d="M3 5h18v14H3z"/><path d="M3 5h18v2l-9 6-9-6z" fill="#f1f0ee"/></svg>
      </li>
      <li class="contact-item">
        <span>www.darvok.nl</span>
        <svg class="contact-icon" viewBox="0 0 24 24" aria-hidden="true"><circle cx="12" cy="12" r="10"/><path d="M8 6c2 1 1 3 3 4s-1 3 1 5M14 18c1-2 3-2 4-4" stroke="#f1f0ee" stroke-width="1.8" fill="none"/></svg>
      </li>
    </ul>
    <p class="brand-name">darvok</p>
  </section>
</div>
</body>
</html>
```